Design a website for our "Bright Stride" Initiative we are implementing at our Youth Soccer Club.

We need a web design for a wellness initiative for our soccer club. "Bright Stride" is the program title. The website will have health and wellness content related to our initiative. It should have interactive features for our users. Videos, survey/data submission capabilities, etc. Colors themed to align with logo. see my start of a website at www.brightstridewithtown.example. I like the homepage design, the rest is unprofessional looking. Design should provide education, tips, advice, resources, for health & wellness; wellness related to our pillars. 6 tabs in addition to home page: Drink more water, fuel your performance, stretch more, protect your skin more, move more, and sports mindset. (year 2 diagram wheel). Sports counseling will be next big focus. Wordpress based website. Easy for me to update in the future.

Target Market(s)

Families with children participating in soccer. concept also applicable to other youth sports.

Industry/Entity Type

Health And Wellness

Number of Pages Required

5+ page

Font styles to use
Sans Serif

Colors
0292cd
f37122

Requirements
Must have
• Bright Stride Logo
• Marrowby Field Soccer Club Logo (*updated*)
• Home page
• Video included that is currently on the website homepage www.brightstridewithtown.example
• Page for each of the 6 pillars
• Focus on "drink more water" pillar and "Mindset" (will focus on sports counseling)
• Flexibility for me to update/edit the website moving forward (non-coding).
• User friendly graphic/picture interface
Nice to have
• Design focused more on the themes, not on soccer. Want the design to be applicable to parents and youth of all sports. Education and interactive features to all ages.

```html
<!DOCTYPE html>
<html lang="en">
<head>
<meta charset="utf-8">
<title>Bright Stride</title>
<link href="https://fonts.googleapis.com/css2?family=Montserrat:wght@400;500;600;700&family=Open+Sans:wght@400;600&display=swap" rel="stylesheet">
<style>
:root{
  --orange:#f58a2a;
  --orange-deep:#f37122;
  --teal:#0b7584;
  --teal-text:#0e6f80;
  --ink:#2b2b2b;
  --body:#5a5a5a;
  --white:#ffffff;
  --line:#1b8a98;
}
*{box-sizing:border-box;margin:0;padding:0}
html,body{width:1200px;height:2432px;overflow:hidden;background:var(--white)}
body{position:relative;font-family:"Montserrat",sans-serif;color:var(--ink)}
.abs{position:absolute}
.topbar{left:0;top:0;width:1200px;height:36px;background:var(--orange)}
.topbar .mail{right:100px;top:9px;color:var(--white);font-size:15px;display:flex;align-items:center;gap:10px;font-weight:500}
.brand{left:0;top:44px;width:1200px;text-align:center}
.brand .dot{width:64px;height:64px;border-radius:50%;background:var(--orange);margin:6px auto 14px}
.brand .name{font-weight:700;font-size:20px;letter-spacing:2px;color:var(--teal-text)}
.nav{left:99px;top:193px;width:1002px;display:flex;justify-content:space-between;font-size:14px;font-weight:500;letter-spacing:1px;color:var(--ink)}
.hero{left:0;top:220px;width:1200px;height:425px;background:linear-gradient(100deg,#6f7b80 0%,#9aa3a5 40%,#c9c2b8 65%,#8f9699 100%)}
.hero h1{position:absolute;left:0;top:150px;width:1200px;text-align:center;color:var(--white);font-size:31px;font-weight:700;line-height:52px;letter-spacing:1px}
.dots{position:absolute;left:578px;top:391px;display:flex;gap:4px}
.dots span{width:11px;height:11px;background:var(--teal)}
.dots span:first-child{background:var(--orange)}
.intro{left:0;top:690px;width:1200px;text-align:center}
.intro h2{color:var(--orange);font-size:29px;font-weight:700;letter-spacing:1px}
.intro .sub{margin-top:14px;font-size:16px;font-weight:500;color:var(--ink)}
.intro p{width:924px;margin:24px auto 0;font-family:"Open Sans",sans-serif;font-size:13px;line-height:21px;color:var(--body);text-align:justify}
.pillar{width:300px;text-align:center}
.pillar .ring{width:76px;height:76px;border:1.5px solid var(--line);border-radius:50%;margin:0 auto 16px;display:flex;align-items:center;justify-content:center}
.pillar .label{font-size:14px;font-weight:500;color:var(--teal-text);letter-spacing:.5px}
.counsel{left:0;top:1281px;width:1200px;height:411px;background:var(--teal)}
.counsel h3{position:absolute;top:48px;width:1200px;text-align:center;color:var(--white);font-size:24px;font-weight:500;letter-spacing:1px}
.tile{position:absolute;display:flex;align-items:center;justify-content:center;color:var(--white);font-weight:600;text-transform:uppercase}
.video{left:99px;top:1732px;width:456px;height:292px;background:linear-gradient(180deg,#000 0 14px,#1c2a33 14px,#2c3d4a 60%,#1e3a22 100%)}
.video .bar{position:absolute;left:10px;right:10px;bottom:28px;height:3px;background:rgba(255,255,255,.35)}
.video .bar i{display:block;width:6%;height:100%;background:#e32}
.video .play{position:absolute;left:22px;bottom:8px}
.video .time{position:absolute;left:100px;bottom:6px;color:var(--white);font-size:11px;font-family:"Open Sans",sans-serif}
.boost{left:603px;top:1762px;width:500px}
.boost h4{font-size:27px;font-weight:500;letter-spacing:1px;color:var(--ink)}
.boost p{margin-top:18px;font-family:"Open Sans",sans-serif;font-size:13px;line-height:20.5px;color:var(--body);text-align:justify}
.btn{display:inline-block;margin-top:24px;background:var(--orange);color:var(--white);font-size:13px;font-weight:600;padding:7px 14px;letter-spacing:.5px}
.club{left:0;top:2310px;width:1200px;display:flex;justify-content:center;align-items:center;gap:10px;font-size:18px;font-weight:700;color:#111}
.club .sq{width:18px;height:18px;background:#111}
.footer{left:0;top:2389px;width:1200px;height:43px;background:var(--teal);color:var(--white);font-size:12px;font-weight:600;text-align:center;line-height:43px;letter-spacing:.5px}
</style>
</head>
<body>
<div class="abs topbar">
  <div class="abs mail">
    <svg width="16" height="12" viewBox="0 0 16 12"><rect x="0" y="0" width="16" height="12" fill="#fff"/><path d="M0 0 L8 7 L16 0" stroke="#f58a2a" stroke-width="1.6" fill="none"/></svg>
    info@brightstride.example
  </div>
</div>

<header class="abs brand">
  <div class="dot"></div>
  <div class="name">BRIGHT STRIDE</div>
</header>

<nav class="abs nav">
  <span>HOME</span><span>DRINK MORE WATER</span><span>FUEL YOUR PERFORMANCE</span><span>STRETCH MORE</span><span>PROTECT YOUR SKIN MORE</span>
  <svg width="14" height="14" viewBox="0 0 14 14"><rect y="2" width="14" height="2" fill="#2b2b2b"/><rect y="6" width="14" height="2" fill="#2b2b2b"/><rect y="10" width="14" height="2" fill="#2b2b2b"/></svg>
</nav>

<section class="abs hero" role="img" aria-label="Photo of a smiling woman with arms outstretched by the sea">
  <h1>MEETING THE SPORTS NUTRITION &amp; EDUCATION<br>NEEDS OF ALL ASPIRING YOUTH ATHLETES</h1>
  <div class="dots"><span></span><span></span><span></span></div>
</section>

<section class="abs intro">
  <h2>BRIGHT STRIDE</h2>
  <div class="sub">Partnership Between Marrowby Field Soccer Club &amp; Lanternway Foundation</div>
  <p>An initiative to help communities develop attitudes and skills to make consistent and positive health-related choices. Promote healthy child development through involvement in sports building a sense of well-being and meeting the growth, development, and activity needs of healthy, confident children and young people. A health and wellness initiative that will educate and provide resources to the players and their families in Marrowby Field Soccer Club. A program that will differentiate Marrowby Field Soccer Club within our community by developing the whole child, on and the field.</p>
</section>

<div class="abs pillar" style="left:137px;top:922px"><div class="ring"><div role="img" aria-label="Water bottle illustration" style="width:22px;height:48px;background:#3a8fd0;border-radius:4px"></div></div><div class="label">Drink More Water</div></div>
<div class="abs pillar" style="left:452px;top:922px"><div class="ring"><div role="img" aria-label="Body figure illustration" style="width:20px;height:56px;background:#2db5c0;border-radius:8px"></div></div><div class="label">Fuel Your Performance</div></div>
<div class="abs pillar" style="left:752px;top:922px"><div class="ring"><div role="img" aria-label="Stretching figure illustration" style="width:70px;height:70px;background:#7cc8ec;border-radius:50%"></div></div><div class="label">Stretch More</div></div>
<div class="abs pillar" style="left:137px;top:1105px"><div class="ring"><div role="img" aria-label="Sneaker illustration" style="width:52px;height:26px;background:#e8603a;border-radius:10px 14px 4px 4px"></div></div><div class="label">Sports Mindset</div></div>
<div class="abs pillar" style="left:463px;top:1105px"><div class="ring"><div role="img" aria-label="Apple illustration" style="width:36px;height:36px;background:#e0443a;border-radius:50%"></div></div><div class="label">Move More</div></div>
<div class="abs pillar" style="left:752px;top:1105px"><div class="ring"><div role="img" aria-label="Illustrated person" style="width:58px;height:58px;background:#f1d3bd;border-radius:50%"></div></div><div class="label">Protect Your Skin More</div></div>

<section class="abs counsel">
  <h3>SPORTS COUNSELING</h3>
  <div class="tile" style="left:99px;top:125px;width:308px;height:242px;background:linear-gradient(135deg,#e9dccb,#c9a88a 60%,#8c6a52)" role="img" aria-label="Photo of a parent and child reading together"></div>
  <div class="tile" style="left:448px;top:125px;width:308px;height:242px;background:linear-gradient(180deg,#7e9a5c,#4f8a3a 50%,#3f7a2c)" role="img" aria-label="Photo of two young boys playing soccer"></div>
  <div class="tile" style="left:792px;top:125px;width:308px;height:242px;background:linear-gradient(135deg,#9c9a64,#8a7a52 60%,#6b6a40);font-size:25px;font-weight:500" role="img" aria-label="Photo of a smiling coach on a field">For Coaches</div>
</section>

<div class="abs video" role="img" aria-label="Video of a coach speaking at a night soccer field">
  <div class="bar"><i></i></div>
  <svg class="play" width="14" height="14" viewBox="0 0 14 14"><path d="M2 1 L13 7 L2 13 Z" fill="#fff"/></svg>
  <span class="time">0:18 / 3:01</span>
</div>

<section class="abs boost">
  <h4>Boost Performance By Adding Color</h4>
  <p>Bright Stride is a partnership between Marrowby Field Soccer Club and the Lanternway Foundation. It is an initiative to help communities develop attitudes and skills to make consistent and positive health-related choices. Promote healthy child development through involvement in sports, building a sense of well-being and meeting the growth, development, and activity needs of healthy, confident children and young people. A health and wellness initiative that will educate and provide resources to the players and their families in Marrowby Field Soccer Club.</p>
  <span class="btn">READ MORE &#9656;</span>
</section>

<div class="abs tile" style="left:154px;top:2089px;width:258px;height:144px;background:linear-gradient(135deg,#5d6366,#8d8f8e 55%,#4b5053);font-size:16px" role="img" aria-label="Photo of a woman drinking water">Drink More Water</div>
<div class="abs tile" style="left:470px;top:2089px;width:258px;height:144px;background:linear-gradient(135deg,#3a4450,#7a6a58 55%,#2d3540);font-size:16px" role="img" aria-label="Photo of a silhouette against the sunset">Mindset</div>
<div class="abs tile" style="left:790px;top:2092px;width:256px;height:144px;background:linear-gradient(135deg,#6e6a64,#5d6a52 55%,#3e4a38);font-size:16px" role="img" aria-label="Photo of a coach watching a football team">Sports Counselling</div>

<div class="abs club"><span class="sq"></span>Marrowby Field Soccer Club</div>

<footer class="abs footer">© 2017 BRIGHT STRIDE. ALL RIGHTS RESERVED.</footer>
</body>
</html>
```